M Zyvantics Buisness Cards

I need a technology focused clean business card for my employees. I have attached out logo to include in the mocks. We're a modern tech consulting firm that drives to interface humanity with technology in a truly cohesive fashion.

```html
<!DOCTYPE html>
<html lang="en">
<head>
<meta charset="UTF-8">
<title>M Zyvantics Business Cards</title>
<link rel="stylesheet" href="https://fonts.googleapis.com/css2?family=Open+Sans:wght@400;600;700&display=swap">
<style>
  :root {
    --page-bg: #eceded;
    --card-white: #ffffff;
    --card-black: #1f1f20;
    --brand-blue: #2f7fd1;
    --brand-grey: #8b8d90;
    --text-light: #ffffff;
    --text-soft: #d6d6d6;
    --shadow: rgba(0, 0, 0, 0.18);
  }
  * { box-sizing: border-box; margin: 0; padding: 0; }
  html, body {
    width: 1200px;
    height: 800px;
    overflow: hidden;
    background: var(--page-bg);
    font-family: "Open Sans", Arial, sans-serif;
  }
  .canvas {
    position: relative;
    width: 1200px;
    height: 800px;
    display: flex;
    align-items: center;
    justify-content: center;
    gap: 40px;
  }
  .card {
    position: relative;
    width: 540px;
    height: 309px;
    border-radius: 3px;
    box-shadow: 0 8px 24px var(--shadow);
    overflow: hidden;
  }
  .card-texture {
    position: absolute;
    inset: 0;
  }
  .card--front { background: var(--card-white); }
  .card--front .card-texture { background: linear-gradient(135deg, #ffffff, #f3f4f5); }
  .card--back { background: var(--card-black); }
  .card--back .card-texture { background: linear-gradient(135deg, #242425, #1b1b1c); }

  .brand {
    position: absolute;
    left: 0;
    right: 0;
    display: flex;
    align-items: center;
    justify-content: center;
    gap: 14px;
  }
  .brand-dot {
    border-radius: 50%;
    border: 5px solid var(--brand-grey);
    flex: none;
  }
  .brand-name {
    font-weight: 600;
    color: var(--brand-grey);
    letter-spacing: 1px;
  }
  .card--front .brand { top: 96px; }
  .card--front .brand-dot { width: 78px; height: 78px; }
  .card--front .brand-name { font-size: 52px; }

  .card--back .brand { top: 40px; }
  .card--back .brand-dot { width: 54px; height: 54px; border-width: 4px; }
  .card--back .brand-name { font-size: 36px; }

  .divider {
    position: absolute;
    left: 0;
    right: 0;
    top: 160px;
    height: 2px;
    background: var(--brand-blue);
  }
  .contact-list {
    position: absolute;
    left: 365px;
    top: 172px;
    list-style: none;
  }
  .contact-item {
    display: flex;
    align-items: center;
    gap: 8px;
    color: var(--text-light);
    font-size: 14px;
    line-height: 22px;
  }
  .contact-icon { width: 14px; height: 14px; flex: none; }
  .person {
    position: absolute;
    left: 44px;
    top: 236px;
    color: var(--text-light);
  }
  .person-name {
    font-size: 22px;
    font-weight: 700;
    letter-spacing: 0.5px;
    line-height: 26px;
  }
  .person-role {
    font-size: 13px;
    color: var(--text-soft);
  }
</style>
</head>
<body>
<main class="canvas">
  <section class="card card--front">
    <div class="card-texture" role="img" aria-label="Faint repeating brand pattern across the card background"></div>
    <div class="brand">
      <span class="brand-dot"></span>
      <span class="brand-name">M Zyvantics</span>
    </div>
  </section>

  <section class="card card--back">
    <div class="card-texture" role="img" aria-label="Subtle dark repeating brand pattern across the card background"></div>
    <div class="brand">
      <span class="brand-dot"></span>
      <span class="brand-name">M Zyvantics</span>
    </div>
    <div class="divider"></div>
    <ul class="contact-list">
      <li class="contact-item">
        <svg class="contact-icon" viewBox="0 0 14 14"><circle cx="7" cy="7" r="7" fill="#2f7fd1"/><path d="M4.3 3.6l1.4-.3.8 1.8-.9.7c.4.9 1.1 1.6 2 2l.7-.9 1.8.8-.3 1.4C7.4 9.1 4.9 6.6 4.3 3.6z" fill="#fff"/></svg>
        (555) 014-2290
      </li>
      <li class="contact-item">
        <svg class="contact-icon" viewBox="0 0 14 14"><circle cx="7" cy="7" r="7" fill="#2f7fd1"/><circle cx="7" cy="7" r="3.8" fill="none" stroke="#fff" stroke-width="0.9"/><ellipse cx="7" cy="7" rx="1.6" ry="3.8" fill="none" stroke="#fff" stroke-width="0.9"/><line x1="3.2" y1="7" x2="10.8" y2="7" stroke="#fff" stroke-width="0.9"/></svg>
        Website
      </li>
      <li class="contact-item">
        <svg class="contact-icon" viewBox="0 0 14 14"><circle cx="7" cy="7" r="7" fill="#2f7fd1"/><rect x="3.5" y="4.5" width="7" height="5" fill="none" stroke="#fff" stroke-width="0.9"/><path d="M3.5 4.5L7 7.3l3.5-2.8" fill="none" stroke="#fff" stroke-width="0.9"/></svg>
        Email
      </li>
    </ul>
    <div class="person">
      <p class="person-name">NAME</p>
      <p class="person-role">Designation</p>
    </div>
  </section>
</main>
</body>
</html>
```